Harbourline Strategy Group firm

I need a business card that is succint for a Brisbane based business called Harbourline Strategy Group Pty Ltd.
We bridge the gaps between People, Process and Technology.

We are a specialist operational excellence firm, delivering strategic consulting and business advisory services in six core capabilities, across all industries and all business lines to improve performance, efficiency, profitability, automation and scalability, for clients across Australia &New Zealand.
Updates

Hi Designers, I have uploaded the logo in 3D .png format, to assist in card design.

Target Market(s)

Project Management professionals, IT professionals, corporate and government clients managing transitioning or transformation projects.

Contact Information for Business Card

Harbourline Strategy Group Pty Ltd

Daniel Ferreira
Principal Consultant

mobile: +61 417 260 315
email: daniel@harbourlinestrategygroup.com.au
webpage: www.harbourlinestrategygroup.com

professional services: strategic advisors,

Font styles to use
Sans Serif

Requirements
Must have
• Business name: Harbourline Strategy Group
logo: attached
Contact person: Daniel Ferreira
Title: Principal Consultant
contact details:
mobile +61 417 260
email: daniel@HarbourlineStrategyGroup.com.au
website: HarbourlineStrategyGroup.com

on back side with logo include: A.B.N. 58210947362

professional services offered: Business Analysis, Strategic Advisory
Nice to have
• QR code
Should not have
• contacts picture

```html
<!DOCTYPE html>
<html lang="en">
<head>
<meta charset="utf-8">
<title>Harbourline Strategy Group – Business Card</title>
<link href="https://fonts.googleapis.com/css2?family=Poppins:wght@400;500;600;700&display=swap" rel="stylesheet">
<style>
  :root {
    --navy: #1f2746;
    --red: #e2242b;
    --white: #ffffff;
    --stage: #1e1f23;
  }
  * { margin: 0; padding: 0; box-sizing: border-box; }
  html, body { width: 1200px; height: 1200px; overflow: hidden; }
  body {
    background: var(--stage);
    font-family: "Poppins", sans-serif;
    position: relative;
  }
  .card {
    position: absolute;
    left: 120px;
    width: 960px;
    height: 540px;
    background: var(--white);
    overflow: hidden;
    border-radius: 4px;
  }
  .card--front { top: 40px; }
  .card--contact { top: 620px; }
  .card__shapes { position: absolute; inset: 0; width: 960px; height: 540px; }

  .brand {
    position: absolute;
    display: flex;
    align-items: center;
    gap: 18px;
  }
  .brand__mark {
    width: 26px; height: 26px;
    border-radius: 50%;
    background: var(--red);
    flex: none;
  }
  .brand__name {
    color: var(--navy);
    font-weight: 700;
    font-size: 46px;
    line-height: 1.02;
    letter-spacing: 1px;
    text-transform: uppercase;
  }
  .card--front .brand { left: 0; right: 0; top: 150px; justify-content: center; }
  .card--contact .brand { right: 70px; top: 120px; }
  .card--contact .brand__name { font-size: 42px; }

  .abn {
    position: absolute;
    top: 320px; left: 0; right: 0;
    text-align: center;
    color: var(--navy);
    font-weight: 500;
    font-size: 24px;
    letter-spacing: 3px;
  }
  .services {
    fill: var(--white);
    font-family: "Poppins", sans-serif;
    font-weight: 500;
    font-size: 25px;
    letter-spacing: 2px;
  }

  .person { position: absolute; left: 70px; top: 238px; }
  .person__name {
    color: var(--navy);
    font-weight: 700;
    font-size: 34px;
    letter-spacing: 1px;
    text-transform: uppercase;
    line-height: 1.1;
  }
  .person__title {
    color: var(--red);
    font-weight: 500;
    font-size: 25px;
    letter-spacing: 1px;
    line-height: 1.2;
  }
  .contacts { list-style: none; margin-top: 16px; }
  .contacts li {
    display: flex;
    align-items: center;
    gap: 14px;
    color: var(--navy);
    font-size: 22px;
    letter-spacing: 0.5px;
    line-height: 36px;
  }
  .contacts svg { width: 26px; height: 26px; flex: none; }
</style>
</head>
<body>

<section class="card card--front" aria-label="Card back side">
  <svg class="card__shapes" viewBox="0 0 960 540" aria-hidden="false">
    <path d="M0,372 Q440,500 960,462 L960,478 Q440,520 0,392 Z" fill="var(--red)"/>
    <path d="M0,392 Q440,520 960,478 L960,540 L0,540 Z" fill="var(--navy)"/>
    <path id="servicesLine" d="M0,428 Q440,556 960,514" fill="none"/>
    <text class="services"><textPath href="#servicesLine" startOffset="50%" text-anchor="middle">Business Analysis | Strategic Advisory</textPath></text>
  </svg>
  <div class="brand">
    <span class="brand__mark"></span>
    <span class="brand__name">Harbourline<br>Strategy Group</span>
  </div>
  <p class="abn">A.B.N. 58210947362</p>
</section>

<section class="card card--contact" aria-label="Card front side">
  <svg class="card__shapes" viewBox="0 0 960 540">
    <path d="M0,0 H640 Q240,40 0,225 Z" fill="var(--navy)"/>
    <path d="M0,170 Q210,28 520,0" fill="none" stroke="var(--white)" stroke-width="30"/>
    <path d="M0,134 Q180,12 420,-4" fill="none" stroke="var(--red)" stroke-width="10"/>
    <path d="M0,420 Q420,530 960,484 L960,500 Q420,550 0,442 Z" fill="var(--red)"/>
    <path d="M0,442 Q420,550 960,500 L960,540 L0,540 Z" fill="var(--navy)"/>
  </svg>

  <div class="brand">
    <span class="brand__mark"></span>
    <span class="brand__name">Harbourline<br>Strategy Group</span>
  </div>

  <div class="person">
    <p class="person__name">Daniel Ferreira</p>
    <p class="person__title">Principal Consultant</p>
    <ul class="contacts">
      <li>
        <svg viewBox="0 0 26 26" aria-hidden="true"><circle cx="13" cy="13" r="11.5" fill="none" stroke="var(--red)" stroke-width="2"/><rect x="9" y="6.5" width="8" height="13" rx="1.5" fill="none" stroke="var(--red)" stroke-width="1.8"/></svg>
        +61 417 260
      </li>
      <li>
        <svg viewBox="0 0 26 26" aria-hidden="true"><circle cx="13" cy="13" r="11.5" fill="none" stroke="var(--red)" stroke-width="2"/><rect x="7" y="9" width="12" height="8.5" fill="none" stroke="var(--red)" stroke-width="1.6"/><path d="M7,9 L13,14 L19,9" fill="none" stroke="var(--red)" stroke-width="1.6"/></svg>
        daniel@HarbourlineStrategyGroup.com.au
      </li>
      <li>
        <svg viewBox="0 0 26 26" aria-hidden="true"><circle cx="13" cy="13" r="11.5" fill="none" stroke="var(--red)" stroke-width="2"/><circle cx="13" cy="13" r="6.5" fill="none" stroke="var(--red)" stroke-width="1.5"/><ellipse cx="13" cy="13" rx="2.8" ry="6.5" fill="none" stroke="var(--red)" stroke-width="1.3"/><path d="M6.5,13 H19.5" stroke="var(--red)" stroke-width="1.3"/></svg>
        HarbourlineStrategyGroup.com
      </li>
    </ul>
  </div>
</section>

</body>
</html>
```